RHS Trifold Brochure

Would like a Trifold Brochure to use for marketing purposes. The company, Reliable Home Solutions is a Handyman Service that offers Residential Home Repairs, Commercial Repairs, Drain Cleaning, Carpet Cleaning and Water Extraction.

I am attaching some pdf files to use as potential verbage and a copy of our business card and logo image file.

Would like to portray a professional image that sets us apart from a "mom and pops" type handyman service.

Industry/Entity Type

Marketing

```html
<!DOCTYPE html>
<html lang="en">
<head>
<meta charset="utf-8">
<title>RHS Trifold Brochure</title>
<link href="https://fonts.googleapis.com/css2?family=Open+Sans:ital,wght@0,400;0,600;0,700;1,700&family=Oswald:wght@500;600&display=swap" rel="stylesheet">
<style>
:root{
  --navy:#14203a;
  --blue:#2a8fd8;
  --sky:#7cc4f0;
  --ink:#262626;
  --paper:#ffffff;
  --stage:#ecebe7;
  --photo-wood:#6b5a45;
  --photo-house:#8aa26a;
  --photo-floor:#b9b2a3;
}
*{box-sizing:border-box;margin:0;padding:0}
html,body{width:1200px;height:543px;overflow:hidden;background:var(--stage);font-family:"Open Sans",Arial,sans-serif;color:var(--ink)}
.spread{position:absolute;top:75px;height:383px;display:flex;box-shadow:0 2px 8px rgba(0,0,0,.25)}
.spread--outside{left:37px;width:541px}
.spread--inside{left:598px;width:542px}
.panel{position:relative;width:33.333%;height:100%;background:var(--paper);overflow:hidden}
.panel + .panel{border-left:1px solid #e3e3e3}
.abs{position:absolute}
.wave{position:absolute;left:0;width:100%}
.photo{position:absolute}
.body{font-size:5.6px;line-height:1.45;text-align:justify}
.body--tight{font-size:5.4px;line-height:1.38}
.h-panel{font-weight:700;text-align:center;color:var(--ink)}
.h-section{font-size:6px;font-weight:700}

/* cover */
.cover__top{position:absolute;left:0;top:0;width:100%;height:175px;background:var(--navy)}
.brand-name{position:absolute;top:45px;left:0;width:100%;text-align:center;color:#fff;font-weight:700;font-size:16px;letter-spacing:.5px}
.brand-sub{position:absolute;top:66px;left:0;width:100%;text-align:center;color:#fff;font-size:7px;letter-spacing:1px}
.cover__title{position:absolute;top:210px;left:0;width:100%;text-align:center;font-family:"Oswald",Arial,sans-serif;color:var(--navy);line-height:.95;font-weight:600}
.cover__title .t1,.cover__title .t2{font-size:15px;display:block}
.cover__title .t3{font-size:24px;display:block}
.cover__tag{position:absolute;top:278px;left:0;width:100%;text-align:center;font-size:5.5px;font-weight:700;color:var(--navy)}
.cover__call{position:absolute;top:326px;left:0;width:100%;text-align:center;font-family:"Oswald",Arial,sans-serif;font-weight:500;color:var(--navy);font-size:12px;line-height:1.5}

/* services list */
.services{position:absolute;top:20px;left:20px;right:8px}
.services dl{display:grid;grid-template-columns:72px 1fr;font-size:5.6px;line-height:1.5;margin-bottom:8px}
.services dt{font-weight:700}
.footer-bar{position:absolute;left:0;bottom:0;width:100%;height:26px;background:var(--navy);color:#fff;font-style:italic;font-weight:700;font-size:9px;display:flex;align-items:center;justify-content:center}
.stripe{position:absolute;left:0;width:100%}
</style>
</head>
<body>

<section class="spread spread--outside">
  <div class="panel cover">
    <div class="cover__top"></div>
    <div class="brand-name">Reliable Home</div>
    <div class="brand-sub">Solutions</div>
    <svg class="wave" style="top:115px" width="180" height="120" viewBox="0 0 180 120" aria-hidden="true">
      <path d="M0 70 C60 40 120 30 180 60 L180 120 L0 120Z" fill="#fff"/>
      <path d="M0 60 C60 25 120 25 180 45 L180 55 C120 38 60 42 0 72Z" fill="var(--blue)"/>
      <path d="M0 74 C60 46 120 42 180 64 L180 68 C120 50 60 54 0 80Z" fill="var(--sky)"/>
    </svg>
    <svg class="wave" style="top:205px" width="180" height="60" viewBox="0 0 180 60" aria-hidden="true">
      <path d="M0 0 C40 10 40 40 0 60Z" fill="var(--navy)" opacity=".15"/>
    </svg>
    <div class="cover__title"><span class="t1">RELIABLE</span><span class="t2">HOME</span><span class="t3">SOLUTIONS</span></div>
    <div class="cover__tag">Service you can count on!!!</div>
    <div class="cover__call">CALL TODAY !!!<br>(555) 014-2290</div>
  </div>

  <div class="panel intro">
    <div class="h-panel abs" style="top:14px;left:0;width:100%;font-size:12px">HANDYMAN SERVICES</div>
    <div class="h-panel abs" style="top:38px;left:12px;right:12px;font-size:8px;line-height:1.3">RELIABLE HOME SOLUTIONS HANDYMAN SERVICES, WHEN YOU JUST NEED TO GET IT DONE!!!</div>
    <div class="stripe" style="top:100px;height:4px;background:var(--blue)"></div>
    <div class="photo" role="img" aria-label="Old hand tools resting in a wooden toolbox" style="top:106px;left:0;width:100%;height:130px;background:linear-gradient(135deg,#3b3026,var(--photo-wood) 55%,#9b8870)"></div>
    <svg class="wave" style="top:218px" width="180" height="40" viewBox="0 0 180 40" aria-hidden="true">
      <path d="M0 10 C60 30 120 30 180 0 L180 40 L0 40Z" fill="#fff"/>
      <path d="M80 25 C120 22 150 14 180 0 L180 8 C150 20 120 28 80 25Z" fill="var(--navy)"/>
    </svg>
    <p class="body body--tight abs" style="top:258px;left:10px;right:8px">Reliable Home Solutions is the answer to your home repair needs. Our staff of experienced technicians have the skills necessary to resolve all of your repair and maintenance issues. Minor Electrical, Plumbing, Heating and Air Conditioning. Honey Do Lists, Painting, Drywall Repair, Locks, Doors, Screens and Windows. Exterior Clean Up, Deck and Siding Repair. Appliance Repairs, Caulking, Tile... you name it we've got you covered</p>
    <div class="abs" style="top:340px;left:0;width:100%;text-align:center;font-style:italic;font-weight:700;font-size:12px">Call Us Today</div>
    <div class="abs" style="top:356px;left:0;width:100%;text-align:center;font-size:6.5px">to see how we can help you!!!</div>
  </div>

  <div class="panel">
    <div class="services">
      <dl><dt>PLUMBING</dt><dd>Faucets<br>Sinks<br>Toilets<br>Garbage Disposals<br>Hot Water Tanks<br>Shut Off Valves<br>Leaks</dd></dl>
      <dl><dt>ELECTRICAL</dt><dd>Lighting<br>Outlets<br>Switches<br>GFCI<br>Ceiling Fans</dd></dl>
      <dl><dt>HVAC &amp; APPLIANCES</dt><dd>Air Conditioning<br>Furnaces<br>Hot Water Heaters<br>Fridges<br>Stoves<br>Dishwashers</dd></dl>
      <dl><dt>INTERIOR SERVICES</dt><dd>Painting<br>Drywall Repair<br>Screens/Windows<br>Locks<br>Tile Repair<br>Tile/Grout Cleaning<br>Caulking<br>Handrails</dd></dl>
      <dl><dt>EXTERIOR SERVICES</dt><dd>Gutter Cleaning<br>Power Washing<br>Deck Repairs<br>Staining/Sealing<br>Wood Rot Repairs<br>Minor Roof Repairs</dd></dl>
    </div>
    <div class="stripe" style="bottom:32px;height:3px;background:var(--sky)"></div>
    <div class="footer-bar">call today !!! &nbsp;(555) 014-2290</div>
  </div>
</section>

<section class="spread spread--inside">
  <div class="panel">
    <div class="h-panel abs" style="top:28px;left:0;width:100%;font-size:7.5px">RIVERTON MAINTENANCE.</div>
    <div class="abs" style="top:42px;left:0;width:100%;text-align:center;font-size:5.8px;line-height:1.55">The services you need.<br>The quality you expect.<br>Prices you can afford!!!</div>
    <p class="body abs" style="top:108px;left:16px;right:12px">Reliable Home Solutions is the professional answer to your all of your home maintenance needs. Our courteous and knowledgable staff have the skills necessary to resolve your issues at a price that you can afford. Reliable Home Solutions offers Handyman Services, Carpet Cleaning, Tile &amp; Grout Cleaning and Drain Cleaning Services. If you are looking for an affordable solutions to your home upkeep needs then give Reliable Home Solutions a call Today and see what we can do for you!!!</p>
    <svg class="wave" style="top:160px" width="180" height="90" viewBox="0 0 180 90" aria-hidden="true">
      <path d="M120 90 C140 50 160 20 180 10 L180 90Z" fill="var(--navy)"/>
      <path d="M110 90 C135 45 158 15 180 2 L180 8 C160 22 140 50 118 90Z" fill="var(--blue)"/>
    </svg>
    <div class="h-section abs" style="top:192px;left:16px">Handyman Service</div>
    <div class="photo" role="img" aria-label="Two-storey house with labelled service areas: roofing, gutters, siding, windows, doors, exterior and interior repairs" style="top:208px;left:14px;width:148px;height:67px;background:linear-gradient(180deg,#6fa7d4,var(--photo-house) 70%,#4e7a3a);border:2px solid #fff"></div>
    <p class="body abs" style="top:285px;left:14px;right:12px">We're here for you! Have a leaky faucet or a toilet that runs? Would you like to hang blinds or repair a hole in the wall? How about a fresh coat of paint in the bathroom? If you don't know how, don't have the time or just don't want to do it yourself give Reliable Home Solutions a call and let us show you what we can do...</p>
    <svg class="wave" style="bottom:0" width="180" height="30" viewBox="0 0 180 30" aria-hidden="true">
      <path d="M0 20 C60 10 120 0 180 4 L180 30 L0 30Z" fill="var(--navy)"/>
    </svg>
  </div>

  <div class="panel">
    <div class="h-section abs" style="top:12px;left:12px">Drain Cleaning Services</div>
    <p class="body abs" style="top:22px;left:12px;right:10px">Reliable Home Solutions can handle all of your drain cleaning needs. Floor Drains, Tub Drains, Toilet, Sinks and Main Sewer Lines, we've got you covered. Reliable Home Solutions's knowledgable technicians have the skills and resources necessary to get you running again. Give us a Call Today to find out about ourservices and affordable prices.</p>
    <div class="photo" role="img" aria-label="Technician clearing a drain with a cleaning machine" style="top:88px;left:14px;width:74px;height:56px;background:linear-gradient(135deg,#cfc8bc,#6e6a63)"></div>
    <div class="photo" role="img" aria-label="Carpet being cleaned with an extraction wand" style="top:88px;left:94px;width:74px;height:56px;background:linear-gradient(135deg,#e2ddd2,#a49d8f)"></div>
    <div class="h-section abs" style="top:154px;left:12px">Carpet Cleaning &amp; Water Extraction</div>
    <p class="body abs" style="top:166px;left:12px;right:10px">Reliable Home Solutions has your carpet cleaning needs covered. The right equipment and the right experience. Whether it is a routine cleaning or deep stain and odor removal we'll make sure you're taken care of. In need of Emergency Water Extraction? We do that too! Give us a Call Today to see what we can do for you..</p>
    <div class="h-section abs" style="top:238px;left:12px">Tile &amp; Grout Cleaning Services</div>
    <div class="photo" role="img" aria-label="Freshly cleaned tile floor" style="top:255px;left:56px;width:70px;height:52px;background:linear-gradient(135deg,#d8d2c6,var(--photo-floor))"></div>
    <p class="body abs" style="top:322px;left:12px;right:10px">You mop and you scrub but is that enough? With our tile and grout cleaning equipment you will truly be amazed with the results. Kitchen and bathroom tile, floor or wall and don't forget the grout. Give us a try, you won't regret it. Call Today and schedule your appointment.</p>
  </div>

  <div class="panel">
    <div class="h-panel abs" style="top:12px;left:0;width:100%;font-size:7px;line-height:1.3">RIVERTON<br>CARPET SERVICE</div>
    <p class="body abs" style="top:35px;left:12px;right:10px">Carpet is one of the most used items in our household and yet is often the most ignored. Dirt, Sand, Food, Dander, Dead Skin, Hair, Grease and oil all build up over time. Sure you vacuum but is it doing enough? The answer is no! Let us take care of your carpet cleaning needs with our experienced technicans and the right equipment for the job.</p>
    <div class="h-panel abs" style="top:104px;left:8px;right:8px;font-size:7px;line-height:1.3">TILE &amp; GROUT CLEANING. THE RESULTS SPEAKS FOR THEMSELVES!!!</div>
    <p class="body abs" style="top:128px;left:12px;right:10px">It only takes once before you are a believer! Tile and grout build up layers of dirt and grime over time. mopping and scrubbing go a long way but from time to time they need a deep clean. That is where Reliable Home Solutions comes in. Regardless of where the tile is we can make a difference for you!</p>
    <div class="h-panel abs" style="top:190px;left:0;width:100%;font-size:7px">EMERGENCY WATER EXTRACTION!!!</div>
    <p class="body abs" style="top:205px;left:12px;right:10px">Water does serious damage. When there is an emergency, timing is of the essence. When that pipe breaks or a back up occurs call us and we'll be there. Our knowledgable staff and is equipped with the resources to give you the best chance of salvaging your carpet after a major water issue. Call Today to see how we can help!!!</p>
    <svg class="wave" style="top:252px" width="180" height="60" viewBox="0 0 180 60" aria-hidden="true">
      <path d="M0 20 C60 0 120 0 180 14 L180 30 C120 16 60 18 0 40Z" fill="var(--navy)"/>
      <path d="M0 40 C60 18 120 16 180 30 L180 36 C120 24 60 26 0 50Z" fill="var(--blue)"/>
    </svg>
    <div class="abs" style="top:316px;left:8px;right:10px;text-align:right;font-style:italic;font-weight:700;font-size:7.5px;color:var(--navy);line-height:1.25">We are Available 24/7 for<br>Emergency Water Extraction!!!</div>
    <svg class="wave" style="bottom:0" width="180" height="34" viewBox="0 0 180 34" aria-hidden="true">
      <path d="M0 10 C60 22 120 18 180 4 L180 34 L0 34Z" fill="var(--navy)"/>
    </svg>
  </div>
</section>

</body>
</html>
```